Bellwood Tax
Project: Business Cards and Stationery
Business Cards and Stationery - Consulting
Business Cards and Stationery
Modern
Peter Marsh
President
28617 Coralind Ave., 4th Floor Sherman Oaks, CA 90572
peterm@bellwdtax.example
www.bellwoodtaxservice.example

```html
<!DOCTYPE html>
<html lang="en">
<head>
<meta charset="utf-8">
<title>Bellwood Tax — Stationery</title>
<link href="https://fonts.googleapis.com/css2?family=Cinzel:wght@500&family=Open+Sans:wght@400;600&display=swap" rel="stylesheet">
<style>
  :root {
    --sky: #3db8ea;
    --sky-light: #c9ecfa;
    --sky-faint: #e6f6fd;
    --paper: #ffffff;
    --ink: #1d2a33;
    --muted: #7a8790;
    --backdrop: #f1f2f3;
    --edge: #dcdfe2;
  }
  * { margin: 0; padding: 0; box-sizing: border-box; }
  html, body { width: 1200px; height: 936px; overflow: hidden; }
  body {
    position: relative;
    background: var(--backdrop);
    font-family: "Open Sans", sans-serif;
    color: var(--ink);
  }
  .sheet { position: absolute; background: var(--paper); border: 1px solid var(--edge); overflow: hidden; }
  .brand { display: flex; align-items: center; gap: 8px; }
  .brand-dot { border-radius: 50%; background: var(--sky); flex: none; }
  .brand-name {
    font-family: "Cinzel", serif; font-weight: 500; color: var(--ink);
    letter-spacing: 0.02em; white-space: nowrap;
  }
  .fine { font-size: 6px; line-height: 1.55; color: var(--muted); white-space: nowrap; }
  .faint-mark { position: absolute; border-radius: 50%; background: var(--sky-faint); }

  /* letterhead */
  .letterhead { left: 182px; top: 68px; width: 425px; height: 544px; }
  .letterhead .brand { position: absolute; left: 26px; top: 30px; }
  .letterhead .brand-dot { width: 26px; height: 26px; }
  .letterhead .brand-name { font-size: 18px; }
  .letterhead .contact { position: absolute; left: 258px; top: 26px; }
  .letterhead .faint-mark { width: 110px; height: 110px; left: 157px; top: 220px; }

  /* folder */
  .folder { left: 633px; top: 30px; width: 425px; height: 582px; background: var(--sky); border: none; }
  .folder-band {
    position: absolute; left: 0; right: 0; top: 210px; height: 128px;
    background: linear-gradient(180deg, #f4f6f7 0%, #ffffff 50%, #eceff1 100%);
    border-top: 3px solid #2a8fc0; border-bottom: 3px solid #2a8fc0;
    display: flex; flex-direction: column; align-items: center; justify-content: center; gap: 10px;
  }
  .folder-band .brand-dot { width: 40px; height: 40px; }
  .folder-band .brand-name { font-size: 30px; }

  /* business cards */
  .card-front { left: 43px; top: 655px; width: 202px; height: 117px; }
  .card-front .brand { position: absolute; left: 12px; top: 12px; gap: 5px; }
  .card-front .brand-dot { width: 12px; height: 12px; }
  .card-front .brand-name { font-size: 10px; }
  .card-front .contact { position: absolute; left: 12px; top: 38px; font-size: 5px; }
  .card-front .holder { font-size: 6px; font-weight: 600; color: var(--ink); }
  .card-back { left: 43px; top: 784px; width: 202px; height: 114px; background: var(--sky); border: none; }
  .card-back .faint-mark { width: 80px; height: 80px; left: 14px; top: 18px; background: rgba(255,255,255,0.18); }

  /* envelope front */
  .envelope { left: 266px; top: 663px; width: 450px; height: 217px; }
  .envelope .brand { position: absolute; left: 16px; top: 16px; gap: 6px; }
  .envelope .brand-dot { width: 16px; height: 16px; }
  .envelope .brand-name { font-size: 13px; }
  .envelope .return { position: absolute; left: 16px; top: 40px; font-size: 5px; }

  /* envelope back */
  .envelope-back { left: 736px; top: 663px; width: 422px; height: 217px; }
  .envelope-back svg { position: absolute; left: 0; top: 0; }
  .envelope-back .url {
    position: absolute; left: 0; right: 0; top: 20px; text-align: center;
    font-size: 8px; letter-spacing: 0.16em; color: #ffffff; text-transform: uppercase;
  }
</style>
</head>
<body>

<section class="sheet letterhead" aria-label="Letterhead">
  <div class="brand"><span class="brand-dot"></span><span class="brand-name">BELLWOOD TAX</span></div>
  <div class="fine contact">
    28617 Coralind Ave., 4th Floor<br>
    Sherman Oaks, CA 90572<br>
    Tel (818) 555-0142<br>
    Fax (818) 555-0143<br>
    peterm@bellwdtax.example<br>
    www.bellwoodtaxservice.example
  </div>
  <div class="faint-mark"></div>
</section>

<section class="sheet folder" aria-label="Presentation folder">
  <div class="folder-band">
    <span class="brand-dot"></span>
    <span class="brand-name">BELLWOOD TAX</span>
  </div>
</section>

<section class="sheet card-front" aria-label="Business card front">
  <div class="brand"><span class="brand-dot"></span><span class="brand-name">BELLWOOD TAX</span></div>
  <div class="fine contact">
    <span class="holder">Peter Marsh</span><br>
    President<br>
    Tel (818) 555-0142<br>
    peterm@bellwdtax.example<br>
    www.bellwoodtaxservice.example
  </div>
</section>

<section class="sheet card-back" aria-label="Business card back">
  <div class="faint-mark"></div>
</section>

<section class="sheet envelope" aria-label="Envelope front">
  <div class="brand"><span class="brand-dot"></span><span class="brand-name">BELLWOOD TAX</span></div>
  <div class="fine return">28617 Coralind Ave., 4th Floor, Sherman Oaks, CA 90572</div>
</section>

<section class="sheet envelope-back" aria-label="Envelope back">
  <svg width="422" height="217" viewBox="0 0 422 217" aria-hidden="true">
    <path d="M0 0 H422 V52 L211 118 L0 52 Z" fill="var(--sky)"/>
    <path d="M0 217 L180 110 M422 217 L242 110" stroke="#e4e7ea" stroke-width="1" fill="none"/>
  </svg>
  <div class="url">www.bellwoodtaxservice.example</div>
</section>

</body>
</html>
```